LABEL DESIGNS FOR SKINCARE LINE

Hello we are needing 12 label various label designs but would like to see you design ONE. We will pick winner from this and send the rest.
LABEL SIZE -2x7
JAR SIZE IS - 8oz
LOGOS FILES BELOW
https://files.pavorna-share.net/drive/folders/7xk3q-wumTrazPLoqVnnRTZBKHAE2DpLW
INFORMATION FOR LABEL
Calm Dune Hush Whipped Body Sugar Scrub 8oz
Ideal for all Skin Types
Ingredients:
Pure Cane Sugar, Extra Virgin Coconut Oil, Mango Butter, Kukum Butter, Emulsifying Wax, Jojoba Seed Oil, Sweet Almond Oil, Strawberry Essential Oil, and Pomegranate Essential Oil.
Directions to use Body Sugar Scrub:
Apply to wet skin gently in a circular motion on desired body area, hands, feet, legs, arms, etc. Once you have a good scrub, rinse, pat dry, and enjoy soft, hydrated skin. Best to use in the shower. Use between 2-3 times a week if needed.
*Cautions:
(1) Allergy: Approach this product with extreme caution, if you have allergies
(2) Avoid direct contact with eyes
Storage/Shelf Life of Product:
For best results, stir/mix scrub with the wooden or plastic spoon before each use. The shelf life of all sugar scrubs is 6-8 weeks. Keep the product in a cool, dry place, away from hot or heated temperatures.
All Natural, Cruelty-Free, Vegan Free
No Mineral Oil
No Petroleum
No Parabens

```html
<!DOCTYPE html>
<html lang="en">
<head>
<meta charset="UTF-8">
<title>Velvet Hollow – Calm Dune Hush Whipped Body Sugar Scrub Label</title>
<link rel="stylesheet" href="https://fonts.googleapis.com/css2?family=Playfair+Display:wght@700&family=Open+Sans:wght@400;600;700&family=Caveat:wght@600&display=swap">
<style>
  :root {
    --page: #f4f2f3;
    --label-pink: #e891ad;
    --panel-white: #ffffff;
    --ink: #2b1c22;
    --rule: #3a2a30;
  }
  * { box-sizing: border-box; margin: 0; padding: 0; }
  html, body { width: 1200px; height: 900px; overflow: hidden; }
  body {
    background: var(--page);
    font-family: "Open Sans", Arial, sans-serif;
    color: var(--ink);
    display: flex; align-items: center; justify-content: center;
  }
  .label {
    width: 1140px; height: 326px;
    background: var(--label-pink);
    display: grid;
    grid-template-columns: 262px 1fr 330px;
    box-shadow: 0 8px 30px rgba(0,0,0,.12);
  }
  .info-panel { padding: 26px 22px; font-size: 10.5px; line-height: 1.45; }
  .info-panel h3 {
    font-size: 10.5px; font-weight: 700; text-transform: uppercase;
    letter-spacing: .3px; margin: 0 0 4px;
  }
  .info-panel p { margin-bottom: 12px; }
  .panel-left { border-right: 1.5px solid var(--rule); }
  .panel-right { border-left: 1.5px solid var(--rule); display: flex; flex-direction: column; }
  .caution-box {
    background: var(--panel-white); padding: 14px 16px; margin-bottom: 16px;
    font-size: 10.5px; line-height: 1.45;
  }
  .caution-box p { margin-bottom: 4px; }

  .front { display: flex; flex-direction: column; align-items: center; padding: 24px 34px 18px; }
  .brand {
    font-family: "Playfair Display", Georgia, serif; font-weight: 700;
    font-size: 52px; line-height: 1.05; color: var(--ink);
  }
  .product-name { margin-top: 10px; text-align: center; font-weight: 600; font-size: 17px; line-height: 1.3; }
  .product-name .ideal { font-weight: 700; }
  .claims { margin-top: 20px; width: 100%; display: flex; align-items: stretch; position: relative; flex: 1; }
  .claims-script { flex: 1; display: flex; flex-direction: column; justify-content: center; gap: 6px; padding-right: 20px; }
  .script-row { display: flex; align-items: center; gap: 10px; }
  .script-row span { font-family: "Caveat", cursive; font-size: 34px; line-height: 1; }
  .claims-divider { width: 1.5px; background: var(--rule); }
  .free-from {
    flex: 1; display: grid; grid-template-columns: 1fr 1fr; gap: 10px 14px;
    padding-left: 22px; align-content: center;
  }
  .free-item { display: flex; flex-direction: column; align-items: center; font-size: 9.5px; font-weight: 600; gap: 3px; }
  .free-item svg { width: 28px; height: 28px; }
  .net-weight { position: absolute; right: 0; bottom: -2px; font-size: 13px; font-weight: 600; }
  .info-panel.storage { padding: 0 22px 22px; }
</style>
</head>
<body>
  <div class="label">
    <section class="info-panel panel-left">
      <h3>Ingredients:</h3>
      <p>Pure Cane Sugar, Extra Virgin Coconut Oil, Mango Butter, Kukum Butter, Emulsifying Wax, Jojoba Seed Oil, Sweet Almond Oil, Strawberry Essential Oil, and Pomegranate Essential Oil.</p>
      <h3>Directions to use Body Sugar Scrub:</h3>
      <p>Apply to wet skin gently in a circular motion on desired body area, hands, feet, legs, arms, etc. Once you have a good scrub, rinse, pat dry, and enjoy soft, hydrated skin. Best to use in the shower. Use between 2-3 times a week if needed.</p>
    </section>

    <section class="front">
      <h1 class="brand">Velvet Hollow</h1>
      <div class="product-name">
        Calm Dune Hush Whipped Body<br>Sugar Scrub<br>
        <span class="ideal">Ideal for ALL SKIN TYPES</span>
      </div>
      <div class="claims">
        <div class="claims-script">
          <div class="script-row">
            <svg width="30" height="30" viewBox="0 0 30 30" fill="none" stroke="#2b1c22" stroke-width="1.6"><path d="M15 4c6 5 7 13 0 22C8 17 9 9 15 4z"/><path d="M15 9v15"/></svg>
            <span>All Natural</span>
          </div>
          <div class="script-row">
            <svg width="30" height="30" viewBox="0 0 30 30" fill="none" stroke="#2b1c22" stroke-width="1.6"><circle cx="15" cy="15" r="12"/></svg>
            <span>Cruelty-Free</span>
          </div>
        </div>
        <div class="claims-divider"></div>
        <div class="free-from">
          <div class="free-item">
            <svg viewBox="0 0 28 28" fill="none" stroke="#2b1c22" stroke-width="1.5"><path d="M14 4c5 7 7 10 7 13a7 7 0 0 1-14 0c0-3 2-6 7-13z"/><path d="M6 22L22 6"/></svg>
            No Mineral Oil</div>
          <div class="free-item">
            <svg viewBox="0 0 28 28" fill="none" stroke="#2b1c22" stroke-width="1.5"><path d="M4 14h20a10 10 0 0 1-20 0z"/><path d="M14 13c0-5 3-8 8-9-1 5-4 8-8 9z"/></svg>
            Vegan Free</div>
          <div class="free-item">
            <svg viewBox="0 0 28 28" fill="none" stroke="#2b1c22" stroke-width="1.5"><path d="M11 4h6M12 4v8l-6 11h16l-6-11V4"/></svg>
            No Parabens</div>
          <div class="free-item">
            <svg viewBox="0 0 28 28" fill="none" stroke="#2b1c22" stroke-width="1.5"><rect x="8" y="6" width="12" height="18" rx="2"/><path d="M8 12h12M8 18h12"/></svg>
            No Petroleum</div>
        </div>
        <span class="net-weight">8oz</span>
      </div>
    </section>

    <section class="panel-right">
      <div class="caution-box">
        <h3 style="font-size:10.5px;margin-bottom:4px;">*CAUTIONS:</h3>
        <p>(1) Allergy: Approach this product with extreme caution, if you have allergies</p>
        <p>(2) Avoid direct contact with eyes</p>
      </div>
      <div class="info-panel storage">
        <h3>Storage/Shelf Life of Product:</h3>
        <p>For best results, stir/mix scrub with the wooden or plastic spoon before each use. The shelf life of all sugar scrubs is 6-8 weeks. Keep the product in a cool, dry place, away from hot or heated temperatures.</p>
      </div>
    </section>
  </div>
</body>
</html>
```